Business Card Design Project for Velora Skin & Medispa

This is a project for a Medispa, where offers service such as massage, facial, IPL treatment, skin rejuvenation. The interior design colour is purple, but I wish not only purple, we can also add some other colour into the design to make it more interesting.

Would be great if the business could be elegant and relaxing feel, instead of the serious business cards. The card is more like a display ticket for customers to park and prevent their card be towed away.

I have uploaded some inspiration samples and logo for your design.

This card will be a general card without any specific person's name on it.
Contents include:
Add: 18C Harlow Ridge Lane, Auckland 1047
P: 09 514 2639
WeChat ID: veloraskinspa
Web: www.veloraskin.example
Updates

Target Market(s)

80% female and 20% male market. Female at all age, mostly asian, but we are trying to expand the market to Kiwis also.

Industry/Entity Type

Business

Font styles to use
Sans Serif
Script

Requirements
Must have
• Floral background or decoration. Prefer watercolour design, but if have any other better idea will do.
To make it unique from other business cards, as it is more for parking display.
Nice to have
• keep is simple as well, please don't put too many different decorations.
Should not have
• Black or dark colour as background.

```html
<!DOCTYPE html>
<html lang="en">
<head>
<meta charset="utf-8">
<title>Velora Skin &amp; Medispa — Business Card</title>
<link rel="stylesheet" href="https://fonts.googleapis.com/css2?family=Dancing+Script:wght@500&family=Raleway:wght@300;400&display=swap">
<style>
  :root {
    --page-bg: #ecebef;
    --lavender: #b7a3d6;
    --lavender-pale: #c9cfe6;
    --lavender-mist: #d6d5ec;
    --orchid: #9b6cc0;
    --plum: #8c4aa6;
    --plum-deep: #7d3f99;
    --blossom: #efeedd;
    --blossom-shade: #b8a9c9;
    --white: #ffffff;
    --frame: rgba(255, 255, 255, 0.55);
  }
  * { margin: 0; padding: 0; box-sizing: border-box; }
  html, body {
    width: 1200px;
    height: 1000px;
    overflow: hidden;
    background: var(--page-bg);
  }
  .canvas {
    width: 1200px;
    height: 1000px;
    display: flex;
    flex-direction: column;
    align-items: center;
    justify-content: center;
    gap: 30px;
  }
  .card {
    position: relative;
    width: 800px;
    height: 457px;
    overflow: hidden;
    box-shadow: 0 4px 18px rgba(60, 40, 90, 0.18);
  }

  /* Front */
  .card-front {
    background: linear-gradient(100deg, var(--lavender) 0%, #bfaedc 35%, var(--lavender-pale) 70%, #cfd3e8 100%);
  }
  .blossom-photo {
    position: absolute;
    inset: 0;
    background:
      radial-gradient(ellipse 28% 34% at 72% 42%, rgba(239, 238, 221, 0.95), rgba(239, 238, 221, 0) 70%),
      radial-gradient(ellipse 22% 26% at 88% 22%, rgba(239, 238, 221, 0.85), rgba(239, 238, 221, 0) 70%),
      radial-gradient(ellipse 26% 22% at 66% 82%, rgba(230, 228, 210, 0.8), rgba(230, 228, 210, 0) 70%),
      radial-gradient(ellipse 40% 18% at 18% 88%, rgba(225, 228, 236, 0.75), rgba(225, 228, 236, 0) 70%),
      radial-gradient(ellipse 20% 20% at 95% 70%, rgba(184, 169, 201, 0.7), rgba(184, 169, 201, 0) 70%);
  }
  .brand-frame {
    position: absolute;
    left: 290px;
    top: 112px;
    width: 196px;
    height: 196px;
    border: 3px solid var(--frame);
    background: rgba(255, 255, 255, 0.18);
    padding: 14px;
  }
  .brand-square {
    width: 100%;
    height: 100%;
    background: var(--orchid);
    display: flex;
    align-items: center;
    justify-content: center;
    text-align: center;
    padding: 10px;
  }
  .brand-name-front {
    font-family: "Raleway", sans-serif;
    font-weight: 300;
    font-size: 24px;
    line-height: 1.3;
    letter-spacing: 1px;
    color: var(--white);
  }

  /* Back */
  .card-back {
    background: linear-gradient(180deg, var(--lavender-mist) 0%, #c9cde6 50%, #b898d2 78%, var(--orchid) 100%);
  }
  .blossom-faint {
    position: absolute;
    inset: 0;
    background:
      radial-gradient(ellipse 18% 30% at 6% 35%, rgba(245, 244, 236, 0.45), rgba(245, 244, 236, 0) 70%),
      radial-gradient(ellipse 16% 24% at 16% 72%, rgba(245, 244, 236, 0.35), rgba(245, 244, 236, 0) 70%),
      radial-gradient(ellipse 12% 18% at 3% 85%, rgba(184, 169, 201, 0.4), rgba(184, 169, 201, 0) 70%);
  }
  .back-content {
    position: absolute;
    inset: 0;
    display: flex;
    flex-direction: column;
    align-items: center;
    padding-top: 54px;
  }
  .brand-name-back {
    font-family: "Raleway", sans-serif;
    font-weight: 400;
    font-size: 17px;
    letter-spacing: 1px;
    color: var(--plum);
  }
  .tagline {
    margin-top: 28px;
    font-family: "Dancing Script", cursive;
    font-weight: 500;
    font-size: 56px;
    color: var(--plum-deep);
    line-height: 1.1;
  }
  .divider {
    margin-top: 18px;
    width: 740px;
    height: 1px;
    background: rgba(255, 255, 255, 0.6);
  }
  .pin-icon {
    margin-top: 14px;
    width: 30px;
    height: 42px;
  }
  .contact {
    margin-top: 8px;
    font-family: "Raleway", sans-serif;
    font-weight: 400;
    font-size: 27px;
    line-height: 1.6;
    color: var(--white);
    text-align: center;
  }
  .contact .sep { padding: 0 8px; }
</style>
</head>
<body>
  <main class="canvas">
    <section class="card card-front" aria-label="Business card front">
      <div class="blossom-photo" role="img" aria-label="Soft-focus photograph of pale cherry blossoms against a lavender sky"></div>
      <div class="brand-frame">
        <div class="brand-square">
          <span class="brand-name-front">Velora Skin &amp; Medispa</span>
        </div>
      </div>
    </section>

    <section class="card card-back" aria-label="Business card back">
      <div class="blossom-faint" role="img" aria-label="Faint blurred cherry blossoms along the left edge"></div>
      <div class="back-content">
        <p class="brand-name-back">Velora Skin &amp; Medispa</p>
        <p class="tagline">Special moments in your life</p>
        <div class="divider"></div>
        <svg class="pin-icon" viewBox="0 0 30 42" aria-hidden="true">
          <path d="M15 1C7.3 1 1 7.2 1 14.8 1 25 15 41 15 41s14-16 14-26.2C29 7.2 22.7 1 15 1z" fill="#ffffff"/>
          <circle cx="15" cy="14.5" r="5" fill="#c9cde6"/>
        </svg>
        <div class="contact">
          <p class="address">18C Harlow Ridge Lane, Auckland 1047</p>
          <p class="phone">Phone: 09.514.2639</p>
          <p class="online">WeChat ID: veloraskinspa<span class="sep">•</span>www.veloraskin.example</p>
        </div>
      </div>
    </section>
  </main>
</body>
</html>
```